International Trading Company, 'KIRO' needs a Business Card

The company name is "KIRO" and it has own logo design.
I'd like to use its logo on this business card.
I need two side Business Card.
I'll look forward to your great design.
Thank you very much in advance.

Contact Information for Business Card

Company Name : Kiro Harbour Limited
Information Example
Dorian Pallister
Mobile(use icon please) : 1 (212) 555-0143
Tel(use icon please) : 1 (212) 555-0178
Email(use icon please) : dorian27@kiroharbour-mail.com
Address(use icon please) : 482 Halden Ave, New York, NY 10160, USA

```html
<!DOCTYPE html>
<html lang="en">
<head>
<meta charset="utf-8">
<title>Kiro Harbour Limited – Business Card</title>
<link rel="stylesheet" href="https://fonts.googleapis.com/css2?family=Arimo:wght@700&family=Tinos&display=swap">
<style>
  :root {
    --backdrop: #d9d9d7;
    --card: #0b0b0b;
    --ink: #6f6f6f;
    --ink-soft: #5a5a5a;
    --accent: #6a6a6a;
  }
  * { margin: 0; padding: 0; box-sizing: border-box; }
  html, body { width: 1200px; height: 1200px; overflow: hidden; }
  body {
    background: var(--backdrop);
    display: flex;
    flex-direction: column;
    align-items: center;
    justify-content: center;
    gap: 60px;
  }
  .card {
    position: relative;
    width: 840px;
    height: 480px;
    background: var(--card);
    box-shadow: 0 6px 18px rgba(0,0,0,0.18);
    overflow: hidden;
  }
  .wordmark {
    font-family: "Arimo", sans-serif;
    font-weight: 700;
    color: var(--ink);
    letter-spacing: 2px;
    line-height: 1;
  }
  .card-back .wordmark {
    position: absolute;
    left: 0; right: 0; top: 50%;
    transform: translateY(-50%);
    text-align: center;
    font-size: 78px;
  }
  .card-front .brand {
    position: absolute;
    left: 0; right: 0; top: 50px;
    text-align: center;
  }
  .card-front .wordmark { font-size: 90px; }
  .company-name {
    margin-top: 6px;
    font-family: "Arimo", sans-serif;
    font-weight: 700;
    font-size: 22px;
    line-height: 1.1;
    color: var(--ink);
    text-transform: uppercase;
    letter-spacing: 0.5px;
  }
  .person-name {
    position: absolute;
    left: 330px; top: 196px;
    font-family: "Tinos", serif;
    font-size: 38px;
    line-height: 44px;
    color: var(--ink);
  }
  .name-rule {
    position: absolute;
    left: 270px; top: 246px;
    width: 360px; height: 7px;
    background: var(--accent);
  }
  .contact-list {
    position: absolute;
    left: 52px; top: 272px;
    list-style: none;
    font-family: "Tinos", serif;
    font-size: 19px;
    color: var(--ink);
  }
  .contact-list li {
    display: flex;
    align-items: center;
    gap: 12px;
    height: 30px;
    white-space: nowrap;
  }
  .contact-list svg { width: 18px; height: 18px; fill: var(--ink-soft); flex: none; }
</style>
</head>
<body>
  <section class="card card-back" aria-label="Card back">
    <div class="wordmark">KIRO</div>
  </section>

  <section class="card card-front" aria-label="Card front">
    <div class="brand">
      <div class="wordmark">KIRO</div>
      <div class="company-name">Kiro Harbour Limited</div>
    </div>

    <div class="person-name">Dorian Pallister</div>
    <div class="name-rule"></div>

    <ul class="contact-list">
      <li>
        <svg viewBox="0 0 24 24" aria-hidden="true"><path d="M12 3 2 12h3v9h5v-6h4v6h5v-9h3z"/></svg>
        482 Halden Ave, New York, NY 10160, USA
      </li>
      <li>
        <svg viewBox="0 0 24 24" aria-hidden="true"><path d="M7 1h10a2 2 0 0 1 2 2v18a2 2 0 0 1-2 2H7a2 2 0 0 1-2-2V3a2 2 0 0 1 2-2zm0 3v14h10V4zm5 15.5a1.2 1.2 0 1 0 0 2.4 1.2 1.2 0 0 0 0-2.4z"/></svg>
        1 (212) 555-0143
      </li>
      <li>
        <svg viewBox="0 0 24 24" aria-hidden="true"><path d="M6.6 10.8a15.1 15.1 0 0 0 6.6 6.6l2.2-2.2a1 1 0 0 1 1-.25 11.4 11.4 0 0 0 3.6.57 1 1 0 0 1 1 1V20a1 1 0 0 1-1 1A17 17 0 0 1 3 4a1 1 0 0 1 1-1h3.5a1 1 0 0 1 1 1c0 1.25.2 2.45.57 3.57a1 1 0 0 1-.25 1z"/></svg>
        1 (212) 555-0178
      </li>
      <li>
        <svg viewBox="0 0 24 24" aria-hidden="true"><path d="M2 5h20v14H2zm2 2v.4l8 5.2 8-5.2V7zm0 2.8V17h16V9.8l-8 5.2z"/></svg>
        dorian27@kiroharbour-mail.com
      </li>
    </ul>
  </section>
</body>
</html>
```